Launch Ledger: How to steer your early capital toward rapid expansion

I need a full-color book cover for a paperback (front, spine and back) in high resolution InDesign and PDF. I also need the derived version for an e-book. Here are some briefing elements:

Audience Profile
Imagine a person standing at the threshold of a significant milestone in their entrepreneurial journey, their heart a mix of excitement and anxiety. Having just secured Series A funding, they acknowledge the validation of their relentless effort and vision but are deeply conscious of the daunting challenges that lie ahead. This individual is navigating the complexities of rapid scaling, managing a larger and potentially more demanding board of directors, and restructuring the company's priorities while preserving its culture. The weight of expectations to succeed and propel the startup to new heights is palpable, stirring a sense of overwhelm amidst the triumph.

Reader Situation
The current state of our target reader might be a mix of excitement and anxiety. Having just secured Series A funding, they recognize the validation of their hard work and vision but are acutely aware of the mountain of challenges ahead. They may feel overwhelmed by the expectations to scale rapidly, manage a larger and potentially more demanding board of directors, and restructure the company's priorities while maintaining its culture. After reading this book and implementing its advice, they would feel empowered, equipped with a clear strategy for tackling the challenges that come with Series A funding, and confident in their ability to scale their startup efficiently. They will be on a promising path toward achieving growth targets necessary for a successful Series B raise, with a newfound understanding of how to manage their team and board dynamics effectively.
Updates

Got some good first attempts on the first round of submissions, I like many of the color schemes proposed and some people have submitted abstract pictures that chime really well with founders who are trying to grow the company.
Where many people fall short is in "Series A playbook" not being the most prominent title on the cover page, picking a picture that does not particularly chime with founders trying to reach higher growth for their company, and sometimes in just throwing some elements on a page and hoping something sticks :)
I'm actively reviewing 3 times per day so please try to follow the briefing and get to the top of the selection list.

Hello everybody, thank you for the designs coming in. There are some entries that are showing great potential! Some clarifications:

- "Series A" and by extension "Series A Playbook" should really be the most prominent part of the cover. If you split it up, make sure "Series A" is together on the same line as it is a term founders will (and must) recognize. If you use different sizes, make sure "Series A" is bigger than "Playbook"
- I much prefer the designs with simpler, more abstract pictures, eg an outline of a person is better than a detailed drawing of a person, but a drawing is still better than a photograph
- Some of you have been using very well known stock photos, we want this to be unique so those designs will not be favored.
- If you do have a person on the cover evoking a startup founder, then put them in clothes that people will recognize: typically a hoody, a tshirt with the logo of their startup, jeans or other comfortable pants, and sneakers. Do not put someone in a suit and tie.
- If you can, use the "footer bar" supplied at the bottom of the front cover to evoke our branding. You can just use the color bars, the logo can be somewhere else.
- The logo should be relatively small and we prefer it to be on the right (because of the arrow in the logo). It should be less prominent than the author name (Teodor Vasquell)
- Finally, I am starting to play closer attention to the spine and the back cover. Spine should be attractive and make it easy to find the book, with author name, title and the Crestway Academy logo (or just the icon). Back cover should have room for a summary, lots of testimonial quotes, a picture of the author and a bar code.

I will check designs daily and give feedback for every design submitted. Thank you all for putting in great work and I'm looking forward to picking a cover shortly!

Target Market(s)

Founders and employees of technology startups in North America, Europe and East Asia

Industry/Entity Type

Startups, technology, software

Font styles to use
Sans Serif

Requirements
Must have
• Dominant title, simple (conceptual) picture, look and feel of practical business book, attractive back cover inviting people to read quotes
Nice to have
• Picture on the front cover that evokes the feeling of having a guide, a map, a navigation tool, so that even if you don't know the exact road, you'll be all right. But ideally keep the picture more abstract and conceptual, I'm not looking for an elaborate illustration
Should not have
• Elaborate illustration, photo on the front cover, complex color scheme

```html
<!DOCTYPE html>
<html lang="en">
<head>
<meta charset="utf-8">
<title>Launch Ledger – Cover Spread</title>
<link href="https://fonts.googleapis.com/css2?family=Bebas+Neue&family=Open+Sans:ital,wght@0,400;0,600;0,700;1,400&display=swap" rel="stylesheet">
<style>
  :root {
    --stage: #000000;
    --paper-light: #f4f3f6;
    --paper-mid: #dcdbe1;
    --paper-dark: #c4c3ca;
    --ink: #2a2a30;
    --ink-soft: #55545c;
    --accent: #e8632b;
    --rule: #b8b7bf;
    --bar-1: #8a8a92;
    --bar-2: #4c6fb3;
    --bar-3: #5aa86a;
    --bar-4: #e8632b;
    --bar-5: #9a64b0;
  }
  * { margin: 0; padding: 0; box-sizing: border-box; }
  html, body { width: 1200px; height: 1200px; overflow: hidden; background: var(--stage); }
  .spread {
    position: absolute; left: 0; top: 166px; width: 1200px; height: 863px;
    background: radial-gradient(ellipse at 30% 25%, var(--paper-light) 0%, var(--paper-mid) 60%, var(--paper-dark) 100%);
    overflow: hidden; font-family: "Open Sans", Arial, sans-serif; color: var(--ink);
  }
  .floor {
    position: absolute; left: 0; right: 0; bottom: 0; height: 300px;
    background: linear-gradient(180deg, rgba(255,255,255,0) 0%, rgba(255,255,255,0.35) 100%);
  }
  .chart { position: absolute; }
  .chart-back { left: 0; top: 60px; width: 290px; height: 260px; }
  .chart-front { left: 985px; top: 620px; width: 215px; height: 180px; }

  /* Back cover */
  .back { position: absolute; left: 0; top: 0; width: 566px; height: 100%; }
  .quote { position: absolute; left: 111px; width: 440px; text-align: center; }
  .quote-text { font-size: 11.5px; font-weight: 700; line-height: 16px; color: var(--ink); }
  .quote-mark { position: absolute; font-family: Georgia, serif; font-weight: 700; font-size: 26px; line-height: 1; color: var(--ink); }
  .quote-mark.open { left: 0; top: -12px; }
  .quote-mark.close { right: 100px; bottom: -14px; }
  .quote-source { font-size: 11px; font-style: italic; color: var(--ink-soft); margin-top: 1px; }
  .quote-rule { position: absolute; left: 209px; width: 178px; height: 1px; background: var(--rule); }

  /* Spine */
  .spine {
    position: absolute; left: 566px; top: 0; width: 62px; height: 100%;
    background: linear-gradient(90deg, rgba(255,255,255,0.35), rgba(255,255,255,0.6), rgba(255,255,255,0.35));
  }
  .spine-sub {
    position: absolute; left: 14px; top: 92px; writing-mode: vertical-rl;
    font-size: 10.5px; font-weight: 600; line-height: 16px; letter-spacing: 0.3px; color: var(--ink); text-transform: uppercase;
  }
  .spine-title {
    position: absolute; left: 19px; top: 365px; writing-mode: vertical-rl;
    font-size: 21px; font-weight: 700; letter-spacing: 4px; color: var(--ink); text-transform: uppercase;
  }
  .spine-brand { position: absolute; left: 17px; top: 708px; display: flex; flex-direction: row; gap: 4px; }
  .spine-brand .brand-square { width: 22px; height: 22px; border: 2px solid var(--ink); }
  .spine-brand-name {
    position: absolute; left: 20px; top: 738px; writing-mode: vertical-rl;
    font-size: 11px; font-weight: 700; letter-spacing: 1.5px; color: var(--ink);
  }

  /* Front cover */
  .front { position: absolute; left: 628px; top: 0; width: 572px; height: 100%; }
  .brand { position: absolute; left: 0; top: 40px; width: 100%; text-align: center; }
  .brand-mark { display: inline-block; width: 42px; height: 42px; border: 3px solid var(--ink); }
  .brand-name { font-size: 31px; font-weight: 700; letter-spacing: 1px; line-height: 36px; margin-top: 6px; color: var(--ink); }
  .brand-sub { font-size: 12px; font-weight: 600; letter-spacing: 7px; color: var(--ink); margin-top: -2px; }
  .title {
    position: absolute; left: 0; top: 162px; width: 100%; text-align: center;
    font-family: "Bebas Neue", "Oswald", Impact, sans-serif; color: var(--accent);
    font-size: 128px; line-height: 110px; letter-spacing: 1px;
  }
  .subtitle {
    position: absolute; left: 0; top: 380px; width: 100%; text-align: center;
    font-size: 19px; line-height: 28px; font-weight: 400; letter-spacing: 0.3px; color: var(--ink); text-transform: uppercase;
  }
  .figure {
    position: absolute; left: 195px; top: 451px; width: 128px; height: 386px;
    background: linear-gradient(180deg, #3a3a40 0%, #26262b 70%, #6d6c74 100%);
    border-radius: 40px 40px 6px 6px; opacity: 0.9;
  }

  .footer-bar { position: absolute; left: 0; bottom: 0; width: 100%; height: 5px; display: flex; }
  .footer-bar span { flex: 1; }
</style>
</head>
<body>
<main class="spread">
  <div class="floor"></div>

  <svg class="chart chart-back" viewBox="0 0 290 260" aria-hidden="true">
    <polyline fill="none" stroke="var(--accent)" stroke-width="3" stroke-linejoin="round"
      points="0,225 10,215 20,222 32,205 40,215 52,200 62,188 70,196 82,180 94,184 104,165 116,172 126,150 136,158 146,140 156,146 168,122 178,130 188,110 198,116 206,96 216,104 224,82 232,88 240,64 248,74 256,56 262,46"/>
    <polygon points="256,28 272,46 254,50" fill="var(--accent)"/>
  </svg>

  <section class="back">
    <div class="quote" style="top:288px">
      <span class="quote-mark open">“</span>
      <p class="quote-text">Lorem ipsum dolor sit amet, consectetuer adipiscing elit, sed diam nonummy nibh euismod tincidunt ut laoreet dolore magna aliquam erat volutpat.</p>
      <p class="quote-source">bane oersib</p>
      <span class="quote-mark close">”</span>
    </div>
    <div class="quote-rule" style="top:386px"></div>
    <div class="quote" style="top:400px">
      <span class="quote-mark open">“</span>
      <p class="quote-text">Lorem ipsum dolor sit amet, consectetuer adipiscing elit, sed diam nonummy nibh euismod tincidunt ut laoreet dolore magna aliquam erat volutpat.</p>
      <p class="quote-source">bane oersib</p>
      <span class="quote-mark close">”</span>
    </div>
    <div class="quote-rule" style="top:520px"></div>
    <div class="quote" style="top:532px">
      <span class="quote-mark open">“</span>
      <p class="quote-text">Lorem ipsum dolor sit amet, consectetuer adipiscing elit, sed diam nonummy nibh euismod tincidunt ut laoreet dolore magna aliquam erat volutpat.</p>
      <p class="quote-source">bane oersib</p>
      <span class="quote-mark close">”</span>
    </div>
    <div class="quote-rule" style="top:650px"></div>
    <div class="quote" style="top:662px">
      <span class="quote-mark open">“</span>
      <p class="quote-text">Lorem ipsum dolor sit amet, consectetuer adipiscing elit, sed diam nonummy nibh euismod tincidunt ut laoreet dolore magna aliquam erat volutpat.</p>
      <p class="quote-source">bane oersib</p>
      <span class="quote-mark close">”</span>
    </div>
  </section>

  <section class="spine">
    <p class="spine-sub">How to steer your early capital<br>toward rapid expansion</p>
    <p class="spine-title">Launch Ledger</p>
    <div class="spine-brand"><span class="brand-square"></span></div>
    <p class="spine-brand-name">CRESTWAY</p>
  </section>

  <section class="front">
    <div class="brand">
      <span class="brand-mark"></span>
      <p class="brand-name">CRESTWAY</p>
      <p class="brand-sub">ACADEMY</p>
    </div>
    <h1 class="title">Launch<br>Ledger</h1>
    <p class="subtitle">How to steer your early capital<br>toward rapid expansion</p>
    <div class="figure" role="img" aria-label="Photograph of a person seen from behind, standing with a briefcase and looking ahead"></div>
  </section>

  <svg class="chart chart-front" viewBox="0 0 215 180" aria-hidden="true">
    <polyline fill="none" stroke="var(--accent)" stroke-width="3" stroke-linejoin="round"
      points="0,150 12,142 22,148 34,130 44,136 56,118 66,124 78,110 90,116 100,96 112,104 122,84 132,90 142,60 152,68 160,40 170,50 178,28 188,42 198,36 215,20"/>
  </svg>

  <div class="footer-bar">
    <span style="background:var(--bar-1)"></span>
    <span style="background:var(--bar-2)"></span>
    <span style="background:var(--bar-3)"></span>
    <span style="background:var(--bar-4)"></span>
    <span style="background:var(--bar-5)"></span>
    <span style="background:var(--bar-4)"></span>
  </div>
</main>
</body>
</html>
```